Custom Landing Page - PHP Development

UPDATE: We do NOT want cartoonish designs. And especially not for this type of graphics: http://snapvue.com/82k3pxq. They're highly popular right now and can be seen on most sites on the internet. Please read the brief carefully before submitting your designs.

We're a software development agency and we're looking to update our PHP development landing page: https://brightloom.software/custom-php-web-development-services

We prepared an improved content section, which can be found here:
https://pages.quillbox.com/document/d/7xQ2mRtV48KLpWzNc3HdYb91EsTaGuJo0fBvXkRiMn/edit?usp=sharing

For the landing page design please use only the content provided in the document above and ignore the content that is currently present on the page.

Other mentions:
- We'd like something dynamic in the above-the-fold area. Currently, there's an animation that's linked to different sections of the page. You'll get bonus points if you can create something animated that looks better than our current solution.
- You don't have to keep the left sidebar. The page can be full-width
- Please keep the main navigation menu and the footer as they currently are
- We're looking for out-of-the-box ideas which don't rely on stock photos! If you use stock photos in your design you'll most likely have a lower chance at winning the project.
- The landing page must be fully mobile-responsive. We'll only consider proposals that cater to this aspect.
- Please be as unique as you can with the graphics you'll be selecting. We really want our site to stand out instead of blending in with other similar sites.

INSPIRATION: Please have a look at these pages to get a feeling for what we're after.
- For the above the fold section: https://layoutharborfeed.com/2019/05/50-creative-landing-page-design-concepts/
- For innovation in website design: https://www.pixelvane.com/

NOTE: We're looking forward to a very long-term collaboration with the right person. So please take your time and put your best foot forward!

Target Market(s)

We're a B2B agency. So our main client are other businesses that require our services. We must convey professionalism and trust.

Industry/Entity Type

Software Development

Number of Pages Required

1 page

Font styles to use
Sans Serif

Requirements
Must have
• We're looking for UNIQUE & INNOVATIVE designs that are not based on stock photos. The design should complement our existing site: Brightloom.software
Nice to have
• It would be great if you could provide a dynamic (animated?) element in the above the fold area.
Should not have
• Please do NOT use stock photos and also AVOID cartoonish graphics such as these: http://snapvue.com/82k3pxq
We don't want a slider in the above-the-fold section.
We're also not keen on dropdown boxes for reading more content (except with the FAQ section).

```html
<!DOCTYPE html>
<html lang="en">
<head>
<meta charset="utf-8">
<title>Brightloom Software – PHP Development Services</title>
<link rel="stylesheet" href="https://fonts.googleapis.com/css2?family=Montserrat:ital,wght@0,300;0,400;0,500;0,600;0,700;0,800;1,400;1,700&display=swap">
<style>
:root{
  --blue:#2360e2;
  --blue-dark:#1b4fc4;
  --orange:#ff4f00;
  --ink:#1d1d2b;
  --grey:#7b7b86;
  --soft:#f4f5fb;
  --white:#ffffff;
  --violet-a:#3410bf;
  --violet-b:#7c14c9;
  --field:#4c0e94;
}
*{box-sizing:border-box;margin:0;padding:0}
html,body{width:678px;height:1200px;overflow:hidden;background:var(--white)}
body{font-family:'Montserrat',sans-serif;color:var(--ink)}
.page{position:absolute;left:0;top:0;width:1455px;height:2576px;transform:scale(0.46598);transform-origin:0 0;overflow:hidden}
.abs{position:absolute}
/* nav */
.nav{position:absolute;left:0;top:0;width:1455px;height:54px;border-bottom:1px solid #e3e4ea;background:var(--white)}
.brand{position:absolute;left:273px;top:16px;display:flex;align-items:center;gap:8px;font-size:16px;font-weight:500;color:var(--ink)}
.brand i{width:22px;height:22px;border-radius:50%;background:var(--blue);display:block}
.nav-link{position:absolute;top:20px;font-size:10.5px;font-weight:700;white-space:nowrap}
.btn-pill{position:absolute;left:1084px;top:11px;width:98px;height:33px;border-radius:17px;background:var(--orange);color:var(--white);font-size:11px;font-weight:700;display:flex;align-items:center;justify-content:center}
/* hero */
.hero-title{left:272px;top:132px;font-size:41px;font-weight:300;line-height:46px;color:#222}
.hero-text{left:273px;top:236px;width:390px;font-size:14.5px;line-height:21px;color:#6f6f78}
.btn{background:var(--orange);color:var(--white);font-weight:700;display:flex;align-items:center;justify-content:center}
.hero-btn{left:273px;top:312px;width:166px;height:45px;font-size:13px}
.play{left:708px;top:242px;width:38px;height:38px}
.hero-art{left:790px;top:75px;width:370px;height:355px;border-radius:24px;background:linear-gradient(145deg,#e8eefb,#b9c8ef 55%,#2d4aa8)}
/* tech band */
.band{left:0;top:442px;width:1455px;height:113px;background:var(--blue)}
.tech{position:absolute;top:30px;width:96px;text-align:center;color:var(--white);font-size:14px;font-weight:600}
.tech i{display:block;margin:0 auto 6px;width:28px;height:28px;border:3px solid var(--white);border-radius:4px}
/* services */
.services{left:0;top:555px;width:1455px;height:910px;background:var(--soft)}
.sec-title{left:272px;top:595px;font-size:36px;font-weight:700;line-height:46px}
.sec-intro{left:743px;top:598px;width:440px;font-size:15.5px;line-height:23px;color:#2a2a35}
.btn-sm{left:741px;top:685px;width:98px;height:32px;font-size:9.5px}
.card{position:absolute;width:210px}
.card .ico{width:48px;height:48px;border-radius:50%;background:var(--blue);display:flex;align-items:center;justify-content:center}
.card h3{margin-top:31px;font-size:14.5px;font-weight:600}
.card p{margin-top:9px;font-size:11px;line-height:16px;color:var(--grey);height:64px}
.card a{display:block;margin-top:17px;font-size:11px;font-weight:700;color:var(--orange)}
/* testimonial */
.photo{position:absolute;border-radius:50%;background:radial-gradient(circle at 50% 40%,#8fa3e6,#3f5fc8 70%)}
.arrow{position:absolute}
.quote{left:372px;top:1661px;width:710px;text-align:center;font-size:11.6px;font-style:italic;line-height:16.8px;color:#333}
.quote-by{left:382px;top:1777px;width:690px;text-align:center;font-size:16px;font-weight:700;font-style:italic}
/* faq */
.faq-panel{left:0;top:1830px;width:686px;height:240px;background:var(--blue)}
.faq-panel h2{position:absolute;left:353px;top:82px;color:var(--white);font-size:25px;font-weight:700;line-height:38px;word-spacing:4px}
.faq-q{position:absolute;left:717px;width:465px;font-size:11px;font-weight:600;display:flex;justify-content:space-between}
.faq-q b{margin-right:6px}
.faq-rule{position:absolute;left:732px;width:447px;height:1px;background:#c7c9d3}
.faq-a{left:738px;top:1978px;width:440px;font-size:10.3px;line-height:21px;color:#555}
/* subscribe */
.sub{left:0;top:2107px;width:1455px;height:68px;background:var(--blue)}
.field-line{position:absolute;top:17px;width:275px;height:32px;border:1px solid #c9d3f4;background:var(--blue-dark);color:#d2dbf8;font-size:11px;padding:9px 15px}
.sub .btn{position:absolute;left:907px;top:18px;width:275px;height:32px;font-size:11px}
/* footer */
.footer{left:0;top:2175px;width:1455px;height:401px;background:linear-gradient(100deg,var(--violet-a),var(--violet-b));color:var(--white)}
.fcol h4{font-size:14.5px;font-weight:700;margin-bottom:14px}
.fcol li{list-style:none;font-size:11px;font-weight:500;margin-bottom:17px}
.contact-row{position:absolute;left:273px;display:flex;gap:14px;font-size:11px;font-weight:500;line-height:23px}
.contact-row i{width:22px;height:22px;border-radius:50%;background:var(--white);display:flex;align-items:center;justify-content:center;flex:none}
.flabel{position:absolute;left:845px;font-size:11px;font-weight:500}
.ffield{position:absolute;left:907px;width:275px;border:1px solid #b9a6ea;background:var(--field)}
.fsubmit{left:907px;top:2460px;width:98px;height:30px;font-size:9px}
.frule{left:273px;top:2515px;width:909px;height:1px;background:#7d5cd8}
.fbottom{top:2537px;font-size:11px;font-weight:500}
.social{left:667px;top:2533px;display:flex;gap:11px}
.social span{width:22px;height:22px;border-radius:50%;background:var(--white)}
</style>
</head>
<body>
<div class="page">

  <header class="nav">
    <div class="brand"><i></i>brightloom.software</div>
    <nav>
      <span class="nav-link" style="left:690px">Products</span>
      <span class="nav-link" style="left:758px">Services</span>
      <span class="nav-link" style="left:823px">Technologies</span>
      <span class="nav-link" style="left:912px">About Us</span>
      <span class="nav-link" style="left:981px">Events</span>
      <span class="nav-link" style="left:1038px">Blog</span>
    </nav>
    <div class="btn-pill">Contact Us</div>
  </header>

  <section class="hero">
    <h1 class="abs hero-title">PHP Development<br>Services</h1>
    <p class="abs hero-text">Brightloom Software is a full-service development agency backed by a vast experience in working with enterprise-level clients.</p>
    <div class="abs btn hero-btn">GET A QUOTE</div>
    <svg class="abs play" viewBox="0 0 38 38"><circle cx="19" cy="19" r="19" fill="#ff4f00"/><path d="M16 14l7 5-7 5z" fill="#fff"/></svg>
    <div class="abs hero-art" role="img" aria-label="Isometric illustration of a laptop with code windows, settings gear and security shield"></div>
  </section>

  <section class="abs band">
    <svg class="arrow" style="left:273px;top:36px" width="24" height="42" viewBox="0 0 24 42"><path d="M21 3L4 21l17 18" stroke="#fff" stroke-width="3" fill="none"/></svg>
    <div class="tech" style="left:327px"><i></i>Script</div>
    <div class="tech" style="left:497px"><i style="border-radius:50%"></i>Mobile</div>
    <div class="tech" style="left:668px"><i></i>Styles</div>
    <div class="tech" style="left:838px"><i></i>Markup</div>
    <div class="tech" style="left:1009px"><i></i>Native</div>
    <svg class="arrow" style="left:1158px;top:36px" width="24" height="42" viewBox="0 0 24 42"><path d="M3 3l17 18L3 39" stroke="#fff" stroke-width="3" fill="none"/></svg>
  </section>

  <section class="abs services"></section>
  <h2 class="abs sec-title">Custom PHP<br>Development Services</h2>
  <p class="abs sec-intro">PHP is one of the most popular development languages for web applications and is one of the core technologies we utilize at Brightloom Software.</p>
  <div class="abs btn btn-sm">READ MORE</div>

  <article class="card" style="left:273px;top:770px"><div class="ico"><svg width="24" height="24" viewBox="0 0 24 24" fill="none" stroke="#fff" stroke-width="1.6"><circle cx="8" cy="12" r="4"/><path d="M14 5h7M14 12h7M14 19h7"/></svg></div><h3>Project takeover</h3><p>Brightloom Software has vast experience in improving websites and web solutions built by other developers.</p><a>READ MORE</a></article>
  <article class="card" style="left:507px;top:770px"><div class="ico"><svg width="26" height="26" viewBox="0 0 24 24" fill="none" stroke="#fff" stroke-width="1.6"><circle cx="12" cy="12" r="10"/><circle cx="12" cy="7" r="1.3" fill="#fff"/><path d="M7 10h10M12 10v4l-3 5M12 14l3 5"/></svg></div><h3>Accessibility</h3><p>Starting from the initial wireframe and roadmap, on through to milestone delivery and beyond, you'll always .....</p><a>READ MORE</a></article>
  <article class="card" style="left:741px;top:770px"><div class="ico"><svg width="24" height="24" viewBox="0 0 24 24" fill="none" stroke="#fff" stroke-width="1.6"><rect x="4" y="4" width="16" height="11" rx="1"/><path d="M2 19h20"/></svg></div><h3>e - Commerce</h3><p>If you plan to start an eCommerce business today, more than ever, you need to have a safe, reliable, and fast e - Commerce shop.</p><a>READ MORE</a></article>
  <article class="card" style="left:972px;top:770px"><div class="ico"><svg width="24" height="24" viewBox="0 0 24 24" fill="none" stroke="#fff" stroke-width="1.6"><rect x="3" y="3" width="10" height="10"/><circle cx="17" cy="17" r="5"/></svg></div><h3>PHP Integration</h3><p>We offer a large selection of PHP integrations to improve your business and ensure a leading position in your niche.</p><a>READ MORE</a></article>

  <article class="card" style="left:273px;top:1005px"><div class="ico"><svg width="24" height="24" viewBox="0 0 24 24" fill="none" stroke="#fff" stroke-width="1.6"><circle cx="9" cy="10" r="4"/><path d="M2 21c1-5 13-5 14 0M15 3h7v5h-7z"/></svg></div><h3>Senior Developers</h3><p>Our senior developers are highly valued software engineers managing enterprise software projects and ensuring clean .....</p><a>READ MORE</a></article>
  <article class="card" style="left:507px;top:1005px"><div class="ico"><svg width="26" height="26" viewBox="0 0 24 24" fill="#fff"><rect x="3" y="15" width="4" height="4"/><rect x="10" y="15" width="4" height="4"/><rect x="17" y="15" width="4" height="4"/><rect x="8" y="4" width="8" height="5" rx="2"/></svg></div><h3 style="font-size:13px">CRM &amp; CMS</h3><p>Brightloom Software delivers on all types of custom PHP projects ranging from web and application development ....</p><a>READ MORE</a></article>
  <article class="card" style="left:740px;top:1005px"><div class="ico"><svg width="24" height="24" viewBox="0 0 24 24" fill="none" stroke="#fff" stroke-width="1.8"><path d="M12 2l8 3v7c0 5-4 8-8 10-4-2-8-5-8-10V5z"/><path d="M8 12l3 3 5-6"/></svg></div><h3>Increased Security</h3><p>Regardless if we're building a small app or enterprise-level, at Brightloom Software, we are very mindful of security concerns.</p><a>READ MORE</a></article>
  <article class="card" style="left:972px;top:1005px"><div class="ico"><svg width="26" height="26" viewBox="0 0 24 24" fill="none" stroke="#fff" stroke-width="1.6"><circle cx="12" cy="12" r="9"/><circle cx="12" cy="12" r="4"/></svg></div><h3>Ongoing Support</h3><p>One of our highest priorities is our clients' complete satisfaction, which we provide with stellar customer support.</p><a style="margin-left:-2px">READ MORE</a></article>

  <article class="card" style="left:507px;top:1232px"><div class="ico"><svg width="24" height="24" viewBox="0 0 24 24" fill="none" stroke="#fff" stroke-width="1.6"><rect x="6" y="2" width="12" height="20" rx="2"/><path d="M10 10l-2 2 2 2M14 10l2 2-2 2"/></svg></div><h3>Mobile Development</h3><p>If you are thinking of creating a messaging app, an online food ordering app.</p><a>READ MORE</a></article>
  <article class="card" style="left:740px;top:1232px"><div class="ico"><svg width="26" height="26" viewBox="0 0 24 24" fill="none" stroke="#fff" stroke-width="1.8"><circle cx="12" cy="12" r="8" stroke-dasharray="3 2"/><path d="M10 10l-2 2 2 2M14 10l2 2-2 2"/></svg></div><h3>Performance Optimisation</h3><p>Website performance that is impacted by complex PHP data structures, incorrect server or system.</p><a>READ MORE</a></article>

  <section class="testimonials">
    <svg class="arrow" style="left:299px;top:1546px" width="16" height="32" viewBox="0 0 16 32"><path d="M14 2L2 16l12 14" stroke="#222" stroke-width="2" fill="none"/></svg>
    <div class="photo" style="left:387px;top:1500px;width:126px;height:126px;opacity:.75" role="img" aria-label="Portrait photo of a client"></div>
    <div class="photo" style="left:653px;top:1483px;width:148px;height:148px" role="img" aria-label="Portrait photo of the featured client"></div>
    <div class="photo" style="left:932px;top:1500px;width:126px;height:126px;opacity:.75" role="img" aria-label="Portrait photo of a client"></div>
    <svg class="arrow" style="left:1131px;top:1546px" width="16" height="32" viewBox="0 0 16 32"><path d="M2 2l12 14L2 30" stroke="#222" stroke-width="2" fill="none"/></svg>
    <p class="abs quote">“ Brightloom Software took ownership on high-priority projects involving backend development for shopcraft1 and cartwell. They also demonstrated ownership working with other folks developing for other ecommerce platform (shopcraft2, storelyne and nodepress). They have deep knowledge about internal of shopcraft1 and helped us from very tricky bugs that otherwise may be unresolved. Furthermore, they are also great communicators that can speak up to fix larger (eg., organizational) problem. They embody our company's culture and we can count on them as teammates. Overall I enjoyed working with them and we already have plan for next project ”</p>
    <p class="abs quote-by">CEO - Pinecrest Checkout</p>
  </section>

  <section class="abs faq-panel"><h2>FREQUENTLY&nbsp; ASKED<br>QUESTIONS</h2></section>
  <div class="faq-q" style="top:1829px"><span><b>01</b>What PHP frameworks do you use ?</span><svg width="14" height="8" viewBox="0 0 14 8"><path d="M1 1l6 6 6-6" stroke="#222" stroke-width="1.5" fill="none"/></svg></div>
  <div class="faq-rule" style="top:1857px"></div>
  <div class="faq-q" style="top:1871px"><span><b>02</b>Why should we select PHP for developing or web applications ?</span><svg width="14" height="8" viewBox="0 0 14 8"><path d="M1 1l6 6 6-6" stroke="#222" stroke-width="1.5" fill="none"/></svg></div>
  <div class="faq-rule" style="top:1899px"></div>
  <div class="faq-q" style="top:1914px"><span><b>03</b>Could we get a mobile first website ?</span><svg width="14" height="8" viewBox="0 0 14 8"><path d="M1 1l6 6 6-6" stroke="#222" stroke-width="1.5" fill="none"/></svg></div>
  <div class="faq-rule" style="top:1941px"></div>
  <div class="faq-q" style="top:1956px"><span><b>04</b>How much time do you need to develop a web application or a website ?</span><svg width="14" height="8" viewBox="0 0 14 8"><path d="M1 7l6-6 6 6" stroke="#222" stroke-width="1.5" fill="none"/></svg></div>
  <p class="abs faq-a">It all depends on the complexity of any given project. For example, developing a static website takes less time compared to a full e - Commerce website. The same applies to web applications. When we start consultations with your team and present your idea to us, we will give you an exact estimate.</p>
  <div class="faq-rule" style="top:2072px"></div>

  <section class="abs sub">
    <div class="field-line" style="left:273px">Name</div>
    <div class="field-line" style="left:590px">E - Mail</div>
    <div class="btn">SUBSCRIBE</div>
  </section>

  <footer class="abs footer"></footer>
  <div class="abs fcol" style="left:308px;top:2218px;color:#fff"><h4>Contact Us</h4></div>
  <div class="contact-row" style="top:2246px;color:#fff"><i><svg width="12" height="12" viewBox="0 0 24 24"><path d="M6 2l4 4-2 3c1 3 4 6 7 7l3-2 4 4-3 4C10 22 2 14 2 5z" fill="#3a10c0"/></svg></i>+1 347 555 0184</div>
  <div class="contact-row" style="top:2282px;color:#fff"><i><svg width="12" height="10" viewBox="0 0 24 18"><rect x="1" y="1" width="22" height="16" fill="none" stroke="#3a10c0" stroke-width="3"/><path d="M1 1l11 9 11-9" fill="none" stroke="#3a10c0" stroke-width="3"/></svg></i>info@brightloom.software</div>
  <div class="contact-row" style="top:2319px;color:#fff"><i><svg width="10" height="13" viewBox="0 0 20 26"><path d="M10 1a9 9 0 00-9 9c0 7 9 15 9 15s9-8 9-15a9 9 0 00-9-9z" fill="#3a10c0"/><circle cx="10" cy="10" r="3" fill="#fff"/></svg></i><span>4120 Rue Larivière Montreal,<br>QC H2K 1P7 Canada</span></div>
  <div class="abs fcol" style="left:523px;top:2218px;color:#fff"><h4>Services</h4><ul><li>Custom Solutions</li><li>Mobile Development</li><li>Web development</li><li>Cloud Services</li><li>BlockChain</li><li>IoT</li><li>Shopcraft Migration</li></ul></div>
  <div class="abs fcol" style="left:710px;top:2218px;color:#fff"><h4>Other links</h4><ul><li style="margin-bottom:24px">About Us</li><li style="margin-bottom:24px">Events</li><li style="margin-bottom:24px">Blog</li><li>Careers</li></ul></div>
  <div class="abs fcol" style="left:907px;top:2218px;color:#fff"><h4>Get In Touch</h4></div>
  <span class="flabel" style="top:2249px;color:#fff">Name</span>
  <div class="ffield" style="top:2252px;height:32px"></div>
  <span class="flabel" style="top:2303px;color:#fff">E - Mail</span>
  <div class="ffield" style="top:2305px;height:32px"></div>
  <span class="flabel" style="top:2359px;color:#fff">Message</span>
  <div class="ffield" style="top:2362px;height:73px"></div>
  <div class="abs btn fsubmit">SUBMIT</div>
  <div class="abs frule"></div>
  <p class="abs fbottom" style="left:273px;color:#fff">© 2012-2021 Brightloom.network. All Rights Reserved</p>
  <div class="abs social" aria-label="Social links"><span></span><span></span><span></span><span></span></div>
  <p class="abs fbottom" style="left:962px;color:#fff">Terms and Conditions &nbsp;&nbsp;|&nbsp;&nbsp;&nbsp; Privacy Policy</p>

</div>
</body>
</html>
```